wooden jewelry - pearl necklaces

I sell wooden jeweler (rings and pearls) on markets, and so on. I also opened my business as a carpenter. The rings and a combination of wood and metal. The wood is special wood, not very common on Europe. I paint the rings afterwards. You can see some of the pictures on the pictures I uploaded. The pearls are made of the same kind of wood and colored in all kinds of colors. They are then assembled to bracelets. The jewelry is very individual and looks really cool and all kinds of people.

Target Market(s)

Young urban alternative with a sense of individuality

Contact Information for Business Card

Front:

Text:

„Kugelwerk“ (big)
„Matthias Oberkirch“ (smaler)

Back
„Holzschmuck
Herstellung von individuellem Holz- und Modeschmuck

Matthias Oberkirch
Tel: 015239460518
Lindmayrweg 27
84489 Burghausen

matthiasoberkirch@postfeld.de“

Font styles to use
Sans Serif

Requirements
Nice to have
• Nice to see a camel thorn tree on the background, this is a special wood and some of the rings are made out of this wood.

```html
<!DOCTYPE html>
<html lang="de">
<head>
<meta charset="utf-8">
<title>Kugelwerk – Visitenkarte</title>
<link rel="stylesheet" href="https://fonts.googleapis.com/css2?family=Montserrat:wght@800;900&family=Jost:wght@300;400&display=swap">
<style>
  :root {
    --backdrop: #e6e1da;
    --bead-dark: #3a2230;
    --bead-warm: #8a4a2c;
    --bead-light: #d9b57c;
    --bead-cream: #efdcb4;
    --wood-deep: #9c4f17;
    --wood-mid: #c06a24;
    --wood-light: #cf7e35;
    --name-brown: #5a2a0c;
    --contact-cream: #f6e3c4;
    --white: #ffffff;
  }
  * { margin: 0; padding: 0; box-sizing: border-box; }
  html, body {
    width: 1200px; height: 895px; overflow: hidden;
    background: var(--backdrop);
  }
  .canvas { position: relative; width: 1200px; height: 895px; }
  .card {
    position: absolute; top: 297px;
    width: 520px; height: 300px;
    border-radius: 16px; overflow: hidden;
    box-shadow: 0 6px 18px rgba(60, 40, 20, 0.25);
  }
  .card--front { left: 50px; }
  .card--back { left: 630px; }

  .bead-photo {
    position: absolute; inset: 0;
    background: linear-gradient(135deg,
      var(--bead-cream) 0%, var(--bead-warm) 22%, var(--bead-dark) 40%,
      var(--bead-light) 58%, var(--bead-warm) 76%, var(--bead-dark) 100%);
  }
  .front-text {
    position: absolute; inset: 0;
    display: flex; flex-direction: column; align-items: center; justify-content: center;
    color: var(--white);
    text-shadow: 0 2px 4px rgba(0,0,0,0.5);
  }
  .brand-name {
    font-family: "Montserrat", sans-serif; font-weight: 900;
    font-size: 50px; letter-spacing: 2px; text-transform: uppercase;
    line-height: 1.1;
  }
  .brand-tagline {
    margin-top: 8px;
    font-family: "Montserrat", sans-serif; font-weight: 900;
    font-size: 20px; letter-spacing: 1px; text-transform: uppercase;
  }

  .wood-surface {
    position: absolute; inset: 0;
    background: linear-gradient(100deg,
      var(--wood-deep) 0%, var(--wood-mid) 35%, var(--wood-light) 60%, var(--wood-mid) 100%);
  }
  .contact {
    position: absolute; inset: 0;
    display: flex; flex-direction: column; align-items: center;
    padding: 26px 24px 0;
    text-align: center;
  }
  .trade {
    font-family: "Jost", sans-serif; font-weight: 400;
    font-size: 13px; letter-spacing: 0.5px;
    color: var(--contact-cream);
    margin-bottom: 12px;
  }
  .trade strong { font-weight: 400; text-transform: uppercase; letter-spacing: 2px; }
  .holder-name {
    font-family: "Montserrat", sans-serif; font-weight: 900;
    font-size: 30px; letter-spacing: 1px; text-transform: uppercase;
    color: var(--name-brown);
    text-shadow: 0 1px 0 rgba(255, 220, 170, 0.35);
    margin-bottom: 12px;
  }
  .contact-icon { width: 22px; height: 18px; margin-bottom: 3px; }
  .contact-line {
    font-family: "Jost", sans-serif; font-weight: 400;
    font-size: 18px; letter-spacing: 1px; line-height: 1.3;
    color: var(--contact-cream);
    margin-bottom: 10px;
  }
</style>
</head>
<body>
<main class="canvas">
  <section class="card card--front">
    <div class="bead-photo" role="img" aria-label="Foto: ein Haufen bunter Holzperlen in Creme, Rotbraun, Rot und Dunkelviolett"></div>
    <div class="front-text">
      <p class="brand-name">Kugelwerk</p>
      <p class="brand-tagline">Custom Made Jewelry</p>
    </div>
  </section>

  <section class="card card--back">
    <div class="wood-surface" role="img" aria-label="Foto: warme, orangebraune Holzmaserung"></div>
    <div class="contact">
      <p class="trade"><strong>Holzschmuck</strong> · Herstellung von individuellem Holz- und Modeschmuck</p>
      <h1 class="holder-name">Matthias Oberkirch</h1>
      <svg class="contact-icon" viewBox="0 0 24 20" aria-hidden="true">
        <path d="M3 6 Q3 2 7 2 L8 2 L9 6 L7 7 Q9 12 15 13 L16 11 L21 12 L21 13 Q21 17 17 17 Q4 16 3 6 Z" fill="var(--name-brown)"/>
      </svg>
      <p class="contact-line">Tel: 015239460518</p>
      <svg class="contact-icon" viewBox="0 0 24 20" aria-hidden="true">
        <path d="M12 1 C7 1 4 4.5 4 8.5 C4 13 12 19 12 19 C12 19 20 13 20 8.5 C20 4.5 17 1 12 1 Z" fill="var(--name-brown)"/>
        <circle cx="12" cy="8.5" r="3" fill="var(--wood-light)"/>
      </svg>
      <p class="contact-line">Lindmayrweg 27 · 84489 Burghausen</p>
      <svg class="contact-icon" viewBox="0 0 24 20" aria-hidden="true">
        <rect x="2" y="3" width="20" height="14" fill="var(--name-brown)"/>
        <path d="M2 3 L12 11 L22 3" fill="none" stroke="var(--wood-light)" stroke-width="1.5"/>
      </svg>
      <p class="contact-line">matthiasoberkirch@postfeld.de</p>
    </div>
  </section>
</main>
</body>
</html>
```